Fitness Equipment Repair Business Needs a Catchy New Business Card

We have an existing business card, however, it is quite plain and boring. We are expanding primarily in the commercial area (gyms, studios, apartment complexes etc). The business card will serve as eye candy to those managers/owners that can't be met for a face to face.
Originally I was planning for a brochure as well, but all of our information is better summarized on our website. (brasswheelservicing.ca).
I would like the card to match the colour scheme of the website and utilize the logo. It should have a professional clean feel to it, however, a little colouring outside the lines wouldn't hurt.
The example card is for my service technician (Corwin Haldane). If possible I would like to be able to edit the text to use for more than one person.

Industry/Entity Type

Appliance Repair

Contact Information for Business Card

Clean, crisp and professional but needs to be eye catching. Preferably using the black, white and red colour scheme matching the website. Double sided would be nice, but is not necessary.

Colors
ec1f27
ffffff
000000

Requirements
Must have
• Must be able to edit name, phone number and title to use for multiple people. Must show the company website (brasswheelservicing.ca).

```html
<!DOCTYPE html>
<html lang="en">
<head>
<meta charset="utf-8">
<title>Brass Wheel Servicing – Business Card</title>
<link href="https://fonts.googleapis.com/css2?family=Lato:wght@400;700&family=Lora:wght@400&display=swap" rel="stylesheet">
<style>
  :root {
    --red: #ec1f27;
    --white: #ffffff;
    --black: #000000;
    --ink: #0b0b0b;
    --backdrop: #e6e6e6;
    --card-w: 540px;
    --card-h: 308px;
  }
  * { box-sizing: border-box; margin: 0; padding: 0; }
  html, body { width: 1200px; height: 900px; overflow: hidden; }
  body {
    background: var(--backdrop);
    font-family: "Lato", sans-serif;
    position: relative;
  }
  .card {
    position: absolute;
    top: 296px;
    width: var(--card-w);
    height: var(--card-h);
    overflow: hidden;
    box-shadow: 0 2px 6px rgba(0,0,0,.18);
  }
  .card--front { left: 40px; background: var(--white); }
  .card--back { left: 620px; background: var(--ink); }
  .card__shapes { position: absolute; inset: 0; width: 100%; height: 100%; }

  /* front */
  .brand {
    position: absolute;
    left: 0; right: 0; top: 70px;
    display: flex; align-items: center; justify-content: center; gap: 12px;
  }
  .brand__dot { width: 22px; height: 22px; border-radius: 50%; background: var(--red); }
  .brand__name {
    font-family: "Lora", serif;
    font-size: 28px;
    color: var(--black);
  }

  /* back */
  .contact-main { position: absolute; left: 40px; top: 112px; }
  .company { font-family: "Lora", serif; color: var(--white); font-size: 19px; }
  .person { color: var(--red); font-weight: 700; font-size: 17px; margin-top: 2px; }
  .contact-list { list-style: none; margin-top: 12px; }
  .contact-list li {
    display: flex; align-items: center; gap: 10px;
    color: var(--white); font-size: 12.5px; line-height: 20px;
  }
  .icon { width: 12px; height: 12px; fill: var(--red); flex: none; }
  .contact-side { position: absolute; left: 330px; top: 112px; }
  .contact-side li { align-items: flex-start; }
  .contact-side .icon { margin-top: 4px; }
  .tagline {
    position: absolute; left: 40px; bottom: 28px;
    font-family: "Lora", serif; color: var(--red); font-size: 14px;
  }
</style>
</head>
<body>

<section class="card card--front" aria-label="Card front">
  <svg class="card__shapes" viewBox="0 0 540 308" aria-hidden="true">
    <polygon points="0,132 160,236 540,236 540,308 0,308" fill="var(--red)"/>
    <polygon points="0,142 158,244 540,244 540,308 0,308" fill="var(--black)"/>
  </svg>
  <div class="brand">
    <span class="brand__dot"></span>
    <span class="brand__name">Brass Wheel Servicing</span>
  </div>
</section>

<section class="card card--back" aria-label="Card back">
  <svg class="card__shapes" viewBox="0 0 540 308" aria-hidden="true">
    <rect width="540" height="308" fill="var(--red)"/>
    <polygon points="0,0 0,308 540,308 540,126 404,0" fill="var(--white)"/>
    <polygon points="0,0 0,308 540,308 540,136 394,0" fill="var(--ink)"/>
  </svg>

  <div class="contact-main">
    <p class="company">Brass Wheel Servicing</p>
    <p class="person">Corwin Haldane</p>
    <ul class="contact-list">
      <li>
        <svg class="icon" viewBox="0 0 12 12"><path d="M2.5 0.5l2 2.2-1 1.3c.8 1.7 2 2.9 3.6 3.6l1.3-1 2.2 2-1.2 2.4C4.8 10.7 1.3 7.2.3 2z"/></svg>
        012 555 0148
      </li>
      <li>
        <svg class="icon" viewBox="0 0 12 12"><path d="M0 2h12v8H0z M0.8 2.6L6 6.6l5.2-4" stroke="var(--ink)" stroke-width="0.9"/></svg>
        info@brasswheelservicing.ca
      </li>
      <li>
        <svg class="icon" viewBox="0 0 12 12"><circle cx="6" cy="6" r="5.2" fill="none" stroke="var(--red)" stroke-width="1.4"/><path d="M1 6h10M6 1v10" stroke="var(--red)" stroke-width="1"/></svg>
        www.brasswheelservicing.ca
      </li>
    </ul>
  </div>

  <ul class="contact-list contact-side">
    <li>
      <svg class="icon" viewBox="0 0 12 12"><path d="M2.5 0.5l2 2.2-1 1.3c.8 1.7 2 2.9 3.6 3.6l1.3-1 2.2 2-1.2 2.4C4.8 10.7 1.3 7.2.3 2z"/></svg>
      012 555 0148
    </li>
    <li>
      <svg class="icon" viewBox="0 0 12 12"><path d="M6 0C3.5 0 1.6 1.9 1.6 4.3 1.6 7.4 6 12 6 12s4.4-4.6 4.4-7.7C10.4 1.9 8.5 0 6 0zm0 6a1.7 1.7 0 110-3.4A1.7 1.7 0 016 6z"/></svg>
      <span>1875 Larkfield Rd NW<br>Edmonton AB T5K2P9</span>
    </li>
  </ul>

  <p class="tagline">When your equipment can't finish the workout, give us a call!</p>
</section>

</body>
</html>
```